business stationery

have a gorgeous logo that needs to be incorporated on stationery. Was hoping to do something on letterhead that was a paper that looked like "bark" from a tree or something that resembled the "woods." Soft paper with some very basic natural elements. Same thing for business cards. Think American lakeside cabin. Organic. Natural. Calm and welcoming but clear to read and understand. Wanted to use alot of black.

Target Market(s)

buyers of Tobias Wrenfield home. Client that would have more than one home and in need of rare pieces and items to furnish an upmarket lakeside holiday cabin in the woods. Someone who treasures beautiful hand made items, organic foods and a real crackling fire but with money to burn in it!

Industry/Entity Type

Business

Requirements
Must have
• My logo
My business name
www.fernandcopper.example
Natural almost raw effect paper
My ABN: 62 307 514 928 (to be placed in small writing at the bottom of card/letterhead)
Nice to have
• The website will consist of a cabin door that you "open" with a creak sound effect and then you go "inside" to look at the various rooms to start shopping. Want to bring that element of texture and warmth into the stationary also.
Should not have
• Anything modern or hard to read items

```html
<!DOCTYPE html>
<html lang="en">
<head>
<meta charset="utf-8">
<title>Fern &amp; Copper — Business Stationery</title>
<link rel="stylesheet" href="https://fonts.googleapis.com/css2?family=Noto+Sans:wght@400;700&family=PT+Sans:wght@400;700&display=swap">
<style>
  :root {
    --backdrop: #808080;
    --paper-light: #eadccf;
    --paper-mid: #e2d2c2;
    --paper-dark: #d9c7b6;
    --ink: #141212;
    --mark-ink: #2a2424;
    --accent: #7a1f1f;
    --muted: #5a5250;
    --black: #000000;
    --white: #ffffff;
  }
  * { margin: 0; padding: 0; box-sizing: border-box; }
  html, body { width: 1200px; height: 1029px; overflow: hidden; background: var(--backdrop); }
  .canvas { position: relative; width: 1200px; height: 1029px; }

  .paper {
    background:
      repeating-linear-gradient(92deg, rgba(255,255,255,0.07) 0 3px, rgba(0,0,0,0.025) 3px 7px),
      linear-gradient(180deg, var(--paper-light), var(--paper-mid) 55%, var(--paper-dark));
  }

  /* Letterhead */
  .letterhead { position: absolute; left: 88px; top: 68px; width: 699px; height: 906px; }
  .letterhead-mark {
    position: absolute; left: 0; right: 0; top: 100px; text-align: center;
    font-family: "Noto Sans", sans-serif; font-weight: 700; font-size: 36px;
    color: var(--mark-ink); letter-spacing: 1px;
  }
  .letter-body {
    position: absolute; left: 86px; top: 230px; width: 511px;
    font-family: "Noto Sans", sans-serif; font-size: 11.4px; line-height: 13.6px;
    color: var(--ink); text-align: justify; hyphens: auto;
  }
  .letter-body p + p { margin-top: 13.6px; }
  .signature-area {
    position: absolute; left: 92px; top: 638px; width: 118px; height: 80px;
    background: rgba(20,18,18,0.08); border-radius: 4px;
  }
  .letter-footer {
    position: absolute; left: 0; right: 0; top: 838px; text-align: center;
    font-family: "PT Sans", sans-serif; font-size: 11.5px; line-height: 14px; color: var(--muted);
  }
  .letter-footer .footer-name { color: var(--accent); }
  .letter-footer .label { color: var(--accent); }
  .letter-footer .gap { display: inline-block; width: 8px; }
  .letterhead-band { position: absolute; left: 0; right: 0; bottom: 0; height: 22px; background: var(--black); }

  /* Business card front */
  .card-front { position: absolute; left: 811px; top: 285px; width: 288px; height: 164px; }
  .card-front .contact-name {
    position: absolute; right: 13px; top: 17px;
    font-family: "PT Sans", sans-serif; font-weight: 700; font-size: 11.5px; color: var(--accent);
  }
  .card-front .contact-role {
    position: absolute; right: 13px; top: 31px;
    font-family: "PT Sans", sans-serif; font-size: 9px; color: var(--muted);
  }
  .card-front .card-mark {
    position: absolute; left: 16px; top: 71px;
    font-family: "Noto Sans", sans-serif; font-weight: 700; font-size: 15px; color: var(--mark-ink);
  }
  .card-front .card-details {
    position: absolute; right: 13px; top: 80px; text-align: right;
    font-family: "PT Sans", sans-serif; font-size: 7px; line-height: 9.6px; color: var(--muted);
  }
  .card-front .card-details .spacer { height: 10px; }
  .card-front .card-details .label { color: var(--accent); font-weight: 700; }
  .card-front .card-band { position: absolute; left: 0; right: 0; bottom: 0; height: 10px; background: var(--black); }

  /* Business card back */
  .card-back {
    position: absolute; left: 811px; top: 462px; width: 288px; height: 165px;
    background: var(--black); color: var(--white); text-align: center;
  }
  .card-back .card-mark {
    position: absolute; left: 0; right: 0; top: 78px;
    font-family: "Noto Sans", sans-serif; font-weight: 700; font-size: 24px;
  }
  .card-back .card-web {
    position: absolute; left: 0; right: 0; top: 117px;
    font-family: "PT Sans", sans-serif; font-size: 10.5px; letter-spacing: 2.4px;
  }
</style>
</head>
<body>
<main class="canvas">

  <section class="letterhead paper" aria-label="Letterhead">
    <div class="letterhead-mark">FERN &amp; COPPER</div>

    <div class="letter-body">
      <p>Lorem ipsum dolor sit amet, consectetuer adipiscing elit. Pellentesque tristique elementum sem. Quisque eget erat ac lectus sodales faucibus. Nam commodo est. Cras consequat faucibus velit. Nam ac magna. Sed et ligula. Nam volutpat, elit ac facilisis tempor, neque augue euismod leo, sit amet molestie sem est eu libero. Nulla facilisi. Pellentesque sit amet odio. Curabitur a leo consectetuer leo blandit porttitor. Pellentesque velit quam, gravida at, pharetra eu, convallis non, sem. Aenean tempor nibh at purus. Pellentesque porta. Suspendisse congue, lacus sit amet imperdiet imperdiet, urna massa rutrum urna, id elementum tellus diam quis risus.</p>
      <p>In dui turpis, varius vitae, tincidunt id, consequat ut, leo. Donec tincidunt tristique odio. Nulla erat felis, euismod nec, fringilla non, aliquet et, magna. Nulla at magna quis nisi pretium vehicula. Pellentesque habitant morbi tristique senectus et netus et malesuada fames ac turpis egestas. Class aptent taciti sociosqu ad litora torquent per conubia nostra, per inceptos himenaeos. In vel quam. Phasellus varius convallis purus. In non turpis. Nam sed risus. Etiam non neque at nisl gravida porttitor. Donec leo dolor, feugiat ut, pharetra et, porttitor a, metus. Suspendisse laoreet magna vel elit. Ut est augue, fermentum ac, molestie at, vestibulum et, urna.</p>
      <p>Nunc purus. Cras auctor. In ornare neque id ipsum. Nulla tincidunt, diam sit amet viverra euismod, sapien augue fringilla neque, at pellentesque felis tortor vel enim. Etiam dignissim. Sed a tortor vel nisl euismod ultricies. Donec molestie congue lectus. Integer sed turpis a tortor imperdiet consequat. Maecenas molestie placerat urna. Sed pede enim, sollicitudin nec, pretium nec, sollicitudin a, felis. In hac habitasse platea dictumst. Nam facilisis, tellus non scelerisque placerat, turpis turpis semper ante, euismod imperdiet augue nisi et neque. Vivamus tincidunt.</p>
      <p>Nulla lobortis ultricies nulla. Pellentesque purus mi, consequat quis, hendrerit sed, imperdiet non, eros. Nullam urna est, vehicula nec, cursus nec, dignissim sit amet, risus. Duis molestie, tellus sit amet laoreet ullamcorper, urna nisi fringilla ante, at rhoncus justo dolor vel dui. Nam hendrerit luctus lorem. Aenean tempor, metus vel posuere gravida, arcu nunc imperdiet tellus, ut blandit sem magna a turpis. Vivamus in neque. Lorem ipsum dolor sit amet, consectetuer adipiscing.</p>
    </div>

    <div class="signature-area" role="img" aria-label="Handwritten signature of the sender"></div>

    <footer class="letter-footer">
      <div class="footer-name">FERN &amp; COPPER</div>
      <div>B2, Larchfield House, 218 Cedar Row, HOLLOWAY Bay 7012</div>
      <div>
        <span class="label">P.</span> 5550 0142<span class="gap"></span>
        <span class="label">F.</span> 5550 0143<span class="gap"></span>
        <span class="label">W.</span> www.fernandcopper.example<span class="gap"></span>
        <span class="label">ABN.</span> 62 307 514 928
      </div>
    </footer>
    <div class="letterhead-band"></div>
  </section>

  <section class="card-front paper" aria-label="Business card front">
    <div class="contact-name">Callum Bretton</div>
    <div class="contact-role">Marketing Manager</div>
    <div class="card-mark">FERN &amp; COPPER</div>
    <div class="card-details">
      <div>B2, Larchfield House, 218 Cedar Row,</div>
      <div>HOLLOWAY Bay 7012</div>
      <div class="spacer"></div>
      <div><span class="label">phone.</span> (55) 01-4470392</div>
      <div><span class="label">fax.</span> (55) 01-4470393</div>
      <div><span class="label">email.</span> hello@fernandcopper.example</div>
      <div><span class="label">ABN.</span> 62 307 514 928</div>
    </div>
    <div class="card-band"></div>
  </section>

  <section class="card-back" aria-label="Business card back">
    <div class="card-mark">FERN &amp; COPPER</div>
    <div class="card-web">www.fernandcopper.example</div>
  </section>

</main>
</body>
</html>
```